Marrowind Radio needs a functional Internet Radio App

We need a Internet Radio app design for IOS and Android,
Shoutcast/ Icecast Stream( SHOUTcast playlist (.pls) file or Icecast (.m3u) playlist file) Supported streams: AAC, AAC+, HE-AAC+.
Should supports TuneBasket, Virtual Dj, Wowza, Auto Dj
Here are some of the features we need you to include in the design:
1. Multi Stream player with Scheduling
2. Track Display
3. Track Sharing ( Chatterbox and other)
4. Album Cover display( automatic cover retrieval base on track)
5.Track Purchases ( Plunkr and Brivex )
6.Push Notification( Geo-localize outgoing data and schedule messages)
7. News, Podcasts and Videos ( Live Feed)
8. Alarms
9. Incorporate "Dedications" ( Listeners love to see when their message is published in real time)
10.Ad management ( management system for the app)
11.Listeners should be able to 'Skip song'
12. Database for music

Target Market(s)

Everyone

Industry/Entity Type

Radio Station

Font styles to use
Decorative

Colors
3176b5
0355a3
85acd3
ffffff

Requirements
Must have
• 1.I need a functional app
• 2. Song Request
Nice to have
• N/A
Should not have
• Other Radio Station app design

```html
<!DOCTYPE html>
<html lang="en">
<head>
<meta charset="utf-8">
<title>Marrowind Radio – My Favorites</title>
<link href="https://fonts.googleapis.com/css2?family=Montserrat:wght@300;400;500;600;700&display=swap" rel="stylesheet">
<style>
  :root {
    --page-bg: #e3e8f0;
    --bar-white: #ffffff;
    --ink: #1c1c1c;
    --nav-blue: #0b3f91;
    --genre-blue: #1a8ae0;
    --search-icon: #1a8ae0;
    --placeholder: #9a9a9a;
    --border: #dcdcdc;
    --tab-bg: #222222;
    --tab-idle: #6a6a6a;
    --tab-active: #ffffff;
  }
  * { box-sizing: border-box; margin: 0; padding: 0; }
  html, body {
    width: 800px; height: 1200px; overflow: hidden;
    background: var(--page-bg);
    font-family: "Montserrat", sans-serif;
    color: var(--ink);
  }
  .showcase-header {
    position: absolute; left: 0; top: 0; width: 800px; height: 64px;
    background: var(--bar-white);
    display: flex; align-items: center; justify-content: space-between;
    padding: 0 18px;
  }
  .showcase-title { font-size: 26px; font-weight: 500; letter-spacing: 0.3px; }
  .showcase-count { font-size: 18px; font-weight: 400; letter-spacing: 0.4px; padding-top: 4px; }

  .app-screen {
    position: absolute; left: 100px; top: 92px; width: 600px; height: 1066px;
    background: #ffffff; overflow: hidden;
    box-shadow: 0 4px 14px rgba(0,0,0,0.08);
  }
  .nav-bar { position: absolute; left: 0; top: 0; width: 600px; height: 102px; background: var(--nav-blue); color: #fff; }
  .status-bar { position: absolute; top: 6px; left: 10px; right: 10px; height: 22px; display: flex; align-items: center; justify-content: space-between; font-weight: 300; font-size: 18px; }
  .status-left, .status-right { display: flex; align-items: center; gap: 6px; }
  .status-time { position: absolute; left: 0; right: 0; text-align: center; }
  .nav-title { position: absolute; top: 52px; width: 100%; text-align: center; font-size: 24px; font-weight: 600; letter-spacing: 0.8px; line-height: 34px; }

  .search-field {
    position: absolute; left: 14px; top: 129px; width: 572px; height: 75px;
    border: 1.5px solid var(--border);
    display: flex; align-items: center; padding-left: 28px; gap: 20px;
  }
  .search-placeholder { font-size: 22px; color: var(--placeholder); letter-spacing: 0.4px; }

  .station-card { position: absolute; width: 280px; }
  .station-art { width: 280px; height: 280px; box-shadow: 0 2px 6px rgba(0,0,0,0.25); }
  .station-name { margin-top: 22px; font-size: 21px; font-weight: 600; letter-spacing: 0.6px; line-height: 26px; }
  .station-genre { margin-top: 6px; font-size: 19px; font-weight: 500; color: var(--genre-blue); letter-spacing: 0.4px; line-height: 24px; }

  .art-pulse { background: linear-gradient(160deg, #5b1f5c 0%, #3d0d3d 60%, #2d0830 100%); }
  .art-nationwide { background: radial-gradient(circle at 40% 40%, #c9b83a 0%, #7a6a2a 35%, #2b2a1c 70%, #d88a7a 100%); }
  .art-pop { background: linear-gradient(170deg, #3a2a22 0%, #a5523a 35%, #c66a4c 65%, #7a3a2a 100%); }
  .art-voltage { background: radial-gradient(circle at 40% 65%, #6a9a8a 0%, #244038 40%, #0e1a18 80%); }

  .tab-bar {
    position: absolute; left: 0; top: 989px; width: 600px; height: 77px;
    background: var(--tab-bg); display: flex;
  }
  .tab-item { flex: 1; display: flex; flex-direction: column; align-items: center; padding-top: 14px; color: var(--tab-idle); font-size: 14px; font-weight: 500; letter-spacing: 0.3px; }
  .tab-item svg { width: 34px; height: 34px; margin-bottom: 10px; }
  .tab-item.is-active { color: var(--tab-active); }
</style>
</head>
<body>
  <header class="showcase-header">
    <span class="showcase-title">Marrowind Radio</span>
    <span class="showcase-count">8 Screens</span>
  </header>

  <main class="app-screen">
    <div class="nav-bar">
      <div class="status-bar">
        <div class="status-left">
          <svg width="56" height="10" viewBox="0 0 56 10"><g fill="#fff"><circle cx="5" cy="5" r="4"/><circle cx="16" cy="5" r="4"/><circle cx="27" cy="5" r="4"/></g><g fill="none" stroke="#fff" stroke-width="1.2"><circle cx="38" cy="5" r="3.6"/><circle cx="49" cy="5" r="3.6"/></g></svg>
          <span>Carrier</span>
          <svg width="18" height="14" viewBox="0 0 18 14"><g fill="none" stroke="#fff" stroke-width="2" stroke-linecap="round"><path d="M2 5a10 10 0 0 1 14 0"/><path d="M5 8a6 6 0 0 1 8 0"/></g><circle cx="9" cy="11.5" r="1.6" fill="#fff"/></svg>
        </div>
        <span class="status-time">3:24 PM</span>
        <div class="status-right">
          <span>100%</span>
          <svg width="40" height="16" viewBox="0 0 40 16"><rect x="0.75" y="0.75" width="35" height="14.5" rx="2" fill="none" stroke="#fff" stroke-width="1.5"/><rect x="3" y="3" width="30.5" height="10" fill="#fff"/><rect x="37" y="5" width="2" height="6" fill="#fff"/></svg>
        </div>
      </div>
      <h1 class="nav-title">MY FAVORITES</h1>
    </div>

    <div class="search-field">
      <svg width="38" height="38" viewBox="0 0 38 38"><circle cx="16" cy="16" r="12" fill="none" stroke="var(--search-icon)" stroke-width="3.5"/><path d="M25 25l9 9" stroke="var(--search-icon)" stroke-width="3.5" stroke-linecap="round"/></svg>
      <span class="search-placeholder">Enter a station or genre</span>
    </div>

    <article class="station-card" style="left:13px; top:232px;">
      <div class="station-art art-pulse" role="img" aria-label="Pulse Tide station artwork: purple concert crowd scene"></div>
      <h2 class="station-name">Pulse Tide!</h2>
      <p class="station-genre">Dance</p>
    </article>
    <article class="station-card" style="left:307px; top:232px;">
      <div class="station-art art-nationwide" role="img" aria-label="Nationwide Radio station artwork: abstract collage in yellow, black and pink"></div>
      <h2 class="station-name">Nationwide Radio</h2>
      <p class="station-genre">Misc</p>
    </article>
    <article class="station-card" style="left:13px; top:619px;">
      <div class="station-art art-pop" role="img" aria-label="POP-HITZ station artwork: warm close-up photo with white sunglasses and painted nails"></div>
      <h2 class="station-name">POP-HITZ</h2>
      <p class="station-genre">Pop</p>
    </article>
    <article class="station-card" style="left:307px; top:619px;">
      <div class="station-art art-voltage" role="img" aria-label="Voltage 94 station artwork: dark photo of headphones and a cap"></div>
      <h2 class="station-name" style="margin-top:24px;">Voltage 94</h2>
      <p class="station-genre">Electronic</p>
    </article>

    <nav class="tab-bar">
      <div class="tab-item">
        <svg viewBox="0 0 34 34" fill="none" stroke="currentColor" stroke-width="1.5"><rect x="3" y="3" width="28" height="28" rx="2"/><rect x="6" y="6" width="22" height="22"/><path d="M14 23V12l8-2v11"/><circle cx="12.5" cy="23" r="1.8"/><circle cx="20.5" cy="21" r="1.8"/></svg>
        <span>Browse</span>
      </div>
      <div class="tab-item is-active">
        <svg viewBox="0 0 34 34" fill="none" stroke="currentColor" stroke-width="1.6" stroke-linecap="round"><circle cx="17" cy="12" r="2.2" fill="currentColor"/><path d="M12 8a6 6 0 0 0 0 8M22 8a6 6 0 0 1 0 8M8 5a10 10 0 0 0 0 14M26 5a10 10 0 0 1 0 14"/><path d="M17 14l-3 17h6z" fill="currentColor"/></svg>
        <span>Favorites</span>
      </div>
      <div class="tab-item">
        <svg viewBox="0 0 34 34" fill="none" stroke="currentColor" stroke-width="1.4"><rect x="3" y="5" width="28" height="26" rx="2"/><path d="M3 11h28M3 17h28M3 23h28M10 11v20M17 11v20M24 11v20M11 3v4M23 3v4"/></svg>
        <span>Schedule</span>
      </div>
      <div class="tab-item">
        <svg viewBox="0 0 34 34" fill="none" stroke="currentColor" stroke-width="1.5"><path d="M17 3c8 0 14 5.5 14 12.5S25 28 17 28c-1.6 0-3-.2-4.4-.6L6 31l1.8-6C5 22.6 3 19.2 3 15.5 3 8.5 9 3 17 3z"/><path d="M15 20V11l6-1.5v8.5"/><circle cx="13.5" cy="20" r="1.6"/><circle cx="19.5" cy="18" r="1.6"/></svg>
        <span>Feed</span>
      </div>
      <div class="tab-item">
        <svg viewBox="0 0 34 34" fill="none" stroke="currentColor" stroke-width="1.5"><rect x="3" y="3" width="28" height="28" rx="2"/><path d="M10 7v20M17 7v20M24 7v20"/><rect x="8" y="18" width="4" height="4" fill="var(--tab-bg)"/><rect x="15" y="11" width="4" height="4" fill="var(--tab-bg)"/><rect x="22" y="15" width="4" height="4" fill="var(--tab-bg)"/></svg>
        <span>Settings</span>
      </div>
    </nav>
  </main>
</body>
</html>
```